maple crest homeworks KOVA

Looking for business card design that represents our company. we are maple crest homeworks and we dedicate our skills of home energy efficiency to our customer by providing energy solution to their energy problems.
HVAC
SOLAR
INSULLATION
LIGHTING
DUCT TESTING
KOVA RATING.

```html
<!DOCTYPE html>
<html lang="en">
<head>
<meta charset="utf-8">
<title>maple crest homeworks — business card</title>
<link rel="stylesheet" href="https://fonts.googleapis.com/css2?family=Arimo:wght@400;700&display=swap">
<style>
  :root {
    --backdrop: #2b2b2b;
    --card-white: #ffffff;
    --card-grey: #e4e4e4;
    --ink-black: #121212;
    --brand-green: #6cbf2a;
    --brand-green-dark: #4f9a1c;
    --text-light: #f2f2f2;
  }
  html, body {
    margin: 0;
    width: 1200px;
    height: 997px;
    overflow: hidden;
    background: var(--backdrop);
    font-family: "Arimo", Arial, sans-serif;
  }
  .sheet {
    position: relative;
    width: 1200px;
    height: 997px;
  }
  .card {
    position: absolute;
    left: 300px;
    width: 600px;
    height: 343px;
    display: block;
  }
  .card--back { top: 110px; }
  .card--front { top: 544px; }
  .logo-name { fill: var(--brand-green); font-weight: 700; font-size: 27px; letter-spacing: 0.5px; }
  .band-heading { fill: var(--text-light); font-weight: 700; font-size: 14px; letter-spacing: 3px; }
  .service { fill: var(--text-light); font-size: 13px; letter-spacing: 1px; }
  .holder-name { fill: var(--text-light); font-weight: 700; font-size: 17px; letter-spacing: 1px; }
  .holder-role { fill: var(--ink-black); font-size: 14px; }
  .contact { fill: var(--text-light); font-size: 15px; letter-spacing: 0.5px; }
  .website { fill: var(--brand-green); font-weight: 700; font-size: 15px; letter-spacing: 0.5px; }
</style>
</head>
<body>
<main class="sheet">
  <svg class="card card--back" viewBox="0 0 600 343" aria-label="Back of business card: services">
    <defs>
      <clipPath id="back-shape"><rect width="600" height="343" rx="22"/></clipPath>
      <linearGradient id="back-paper" x1="0" y1="0" x2="0" y2="1">
        <stop offset="0" stop-color="var(--card-white)"/>
        <stop offset="1" stop-color="var(--card-grey)"/>
      </linearGradient>
    </defs>
    <g clip-path="url(#back-shape)">
      <rect class="paper" width="600" height="343" fill="url(#back-paper)"/>
      <polygon class="accent-band" points="0,228 150,228 185,172 415,172 450,228 600,228 600,245 0,245" fill="var(--brand-green)"/>
      <polygon class="dark-base" points="0,240 160,240 192,200 408,200 440,240 600,240 600,343 0,343" fill="var(--ink-black)"/>
      <polygon class="accent-band-shade" points="185,172 415,172 408,200 192,200" fill="var(--brand-green-dark)" opacity="0.35"/>
    </g>
    <g class="logo-lockup">
      <rect x="150" y="42" width="300" height="100" rx="10" fill="var(--ink-black)" stroke="var(--brand-green)" stroke-width="3"/>
      <circle cx="186" cy="92" r="14" fill="var(--brand-green)"/>
      <text class="logo-name" x="210" y="85">maple crest</text>
      <text class="logo-name" x="210" y="117">homeworks</text>
    </g>
    <text class="band-heading" x="300" y="192" text-anchor="middle">OUR SERVICES</text>
    <g class="services services--left">
      <circle cx="180" cy="252" r="3.5" fill="var(--brand-green)"/><text class="service" x="192" y="257">HVAC</text>
      <circle cx="180" cy="276" r="3.5" fill="var(--brand-green)"/><text class="service" x="192" y="281">SOLAR</text>
      <circle cx="180" cy="300" r="3.5" fill="var(--brand-green)"/><text class="service" x="192" y="305">INSULLATION</text>
    </g>
    <g class="services services--right">
      <text class="service" x="408" y="257" text-anchor="end">LIGHTING</text><circle cx="420" cy="252" r="3.5" fill="var(--brand-green)"/>
      <text class="service" x="408" y="281" text-anchor="end">DUCT TESTING</text><circle cx="420" cy="276" r="3.5" fill="var(--brand-green)"/>
      <text class="service" x="408" y="305" text-anchor="end">KOVA RATING</text><circle cx="420" cy="300" r="3.5" fill="var(--brand-green)"/>
    </g>
  </svg>

  <svg class="card card--front" viewBox="0 0 600 343" aria-label="Front of business card: contact details">
    <defs>
      <clipPath id="front-shape"><rect width="600" height="343" rx="22"/></clipPath>
      <linearGradient id="front-paper" x1="0" y1="0" x2="0" y2="1">
        <stop offset="0" stop-color="var(--card-white)"/>
        <stop offset="1" stop-color="var(--card-grey)"/>
      </linearGradient>
    </defs>
    <g clip-path="url(#front-shape)">
      <rect class="paper" width="600" height="343" fill="url(#front-paper)"/>
      <polygon class="accent-band" points="0,222 165,222 200,162 430,162 460,140 600,140 600,215 0,240" fill="var(--brand-green)"/>
      <polygon class="dark-base" points="0,232 175,232 205,205 600,190 600,343 0,343" fill="var(--ink-black)"/>
      <polygon class="accent-band-shade" points="430,162 460,140 600,140 600,150 470,150" fill="var(--brand-green-dark)" opacity="0.5"/>
    </g>
    <g class="logo-lockup">
      <rect x="150" y="32" width="300" height="100" rx="10" fill="var(--ink-black)" stroke="var(--brand-green)" stroke-width="3"/>
      <circle cx="186" cy="82" r="14" fill="var(--brand-green)"/>
      <text class="logo-name" x="210" y="75">maple crest</text>
      <text class="logo-name" x="210" y="107">homeworks</text>
    </g>
    <text class="holder-name" x="310" y="181" text-anchor="middle">DANIEL WHITMORE</text>
    <text class="holder-role" x="310" y="199" text-anchor="middle">Managing Director</text>
    <text class="website" x="575" y="222" text-anchor="end">www.maplecresthome.com</text>
    <g class="contact-list">
      <g class="contact-item">
        <circle cx="34" cy="266" r="10" fill="var(--card-grey)"/>
        <path d="M29,263 q5,-4 10,0 l-1.5,2 h-2 v-1.5 h-3 v1.5 h-2 z M30,267 h8 v3 h-8 z" fill="var(--ink-black)"/>
        <text class="contact" x="54" y="271">0400555018</text>
      </g>
      <g class="contact-item">
        <circle cx="34" cy="293" r="10" fill="var(--card-grey)"/>
        <rect x="28" y="289" width="12" height="8" fill="none" stroke="var(--ink-black)" stroke-width="1.5"/>
        <path d="M28,289 l6,5 l6,-5" fill="none" stroke="var(--ink-black)" stroke-width="1.5"/>
        <text class="contact" x="54" y="298">dan@maplecrest.biz</text>
      </g>
      <g class="contact-item">
        <circle cx="34" cy="320" r="10" fill="var(--card-grey)"/>
        <path d="M34,327 l-5,-7 a5,5 0 1,1 10,0 z" fill="var(--brand-green)"/>
        <circle cx="34" cy="318" r="1.8" fill="var(--card-grey)"/>
        <text class="contact" x="54" y="317">PO Box 318 Kelvale</text>
        <text class="contact" x="54" y="335">B.C. QLD 4350</text>
      </g>
    </g>
  </svg>
</main>
</body>
</html>
```